Trevo SnapKiosk

Hi There,

I am looking to rebuild my company website.

Here are the development specs for my new site!:

1) I've designed a layout for my site and am looking for someone to incorporate the graphics into a word press template. Enclosed is a screen grab of the look and feel (all of the images / graphic working files are available).

2) The site needs to be built on a wordpress platform so that I can regularly edit the site content and make changes / updates

4) The web content (text) has not been finalized and is still being created. For now, I would really like to get the site developed (from a functionality standpoint) and provide text for each page as we finalize the site development.

I'm really excited to get my site redeveloped and launched!

Industry/Entity Type

It Company

Requirements
Must have
• Home Page to have rotating images

```html
<!DOCTYPE html>
<html lang="en">
<head>
<meta charset="utf-8">
<title>Trevo SnapKiosk</title>
<link href="https://fonts.googleapis.com/css2?family=Ubuntu:wght@400;500;700&family=Fjalla+One&family=Rokkitt:wght@700&display=swap" rel="stylesheet">
<style>
:root{
  --ink:#1e1e1e;
  --band:#17181a;
  --panel:#242528;
  --brand-blue:#5a7cbf;
  --headline-blue:#3f73dc;
  --accent:#a3195b;
  --rule:#555;
  --nav-top:#4a4a4a;
  --nav-bottom:#1f1f1f;
  --footer:#efefef;
  --icon:#c9c9c9;
}
*{margin:0;padding:0;box-sizing:border-box}
html,body{width:927px;height:1200px;overflow:hidden;background:#fff}
body{position:relative;font-family:Ubuntu,sans-serif;color:var(--ink)}
.brand{position:absolute;left:23px;top:42px;display:flex;align-items:center;gap:12px}
.brand-dot{width:44px;height:44px;border-radius:50%;background:var(--brand-blue)}
.brand-name{font-family:Ubuntu,sans-serif;font-weight:700;font-size:30px;color:#555;letter-spacing:-0.5px}
.main-nav{position:absolute;left:321px;top:105px;height:42px;display:flex;border:1px solid #000;border-bottom:none;border-top:2px solid #888}
.main-nav a{display:flex;align-items:center;justify-content:center;height:40px;padding:0 22px;color:#fff;text-decoration:none;font-size:12px;text-transform:uppercase;background:linear-gradient(var(--nav-top),var(--nav-bottom));border-right:1px solid #000;border-left:1px solid #5a5a5a}
.hero-band{position:absolute;left:0;top:147px;width:927px;height:311px;background:var(--band)}
.slider{position:absolute;left:38px;top:189px;width:851px;height:328px;background:var(--panel);box-shadow:0 8px 14px rgba(0,0,0,.45)}
.slide-photo{position:absolute;left:16px;top:18px;width:499px;height:281px;background:#fff}
.slide-photo div{position:absolute;left:30px;top:8px;width:440px;height:265px;background:linear-gradient(135deg,#c9a692,#6c6c6c 55%,#2e2e2e)}
.slide-title{position:absolute;left:533px;top:18px;font-family:"Fjalla One",sans-serif;font-size:37px;color:var(--headline-blue);letter-spacing:.5px}
.slide-copy{position:absolute;left:535px;top:68px;width:298px;font-size:13.6px;line-height:20.8px;color:#fff}
.know-more{position:absolute;left:681px;top:262px;width:149px;height:37px;background:linear-gradient(#4f7ee0,#2c55b5);color:#fff;font-family:Rokkitt,serif;font-weight:700;font-size:16px;display:flex;align-items:center;justify-content:center;gap:8px}
.dots{position:absolute;left:222px;top:310px;display:flex;gap:7px}
.dots span{width:8px;height:8px;border-radius:50%;background:#bbb}
.dots span.active{background:#d21d1d}
.section-title{position:absolute;left:43px;top:536px;font-weight:700;font-size:25px;letter-spacing:.5px}
.rule{position:absolute;left:37px;width:847px;border-top:1px dashed var(--rule)}
.quote{position:absolute;left:37px;width:650px;font-family:Tahoma,Verdana,sans-serif;font-size:11.2px;line-height:15.2px;color:#222}
.portrait{position:absolute;left:703px;width:177px;height:115px;border:1px solid #d5d5d5;padding:4px;background:#fff;box-shadow:0 1px 2px rgba(0,0,0,.1)}
.portrait div{width:100%;height:100%}
.author{position:absolute;left:37px;font-weight:700;font-size:13px;color:var(--accent);text-transform:uppercase}
.site-footer{position:absolute;left:0;top:1145px;width:927px;height:55px;background:linear-gradient(#f7f7f7,#e8e8e8);border-top:1px solid #ddd}
.copyright{position:absolute;left:46px;top:27px;font-family:Arial,sans-serif;font-size:10px;color:#222}
.keep-touch{position:absolute;left:644px;top:24px;font-size:13px;font-weight:700;color:#333}
.social{position:absolute;left:754px;top:18px;display:flex;gap:12px}
.social span{width:23px;height:23px;border-radius:50%;background:var(--icon)}
</style>
</head>
<body>
<header>
  <div class="brand"><span class="brand-dot"></span><span class="brand-name">Trevo SnapKiosk</span></div>
  <nav class="main-nav">
    <a href="#">Home</a><a href="#">Services</a><a href="#">Testimonials</a><a href="#">Album Gallery</a><a href="#">Blog</a><a href="#">Contact</a>
  </nav>
</header>

<div class="hero-band"></div>
<section class="slider">
  <div class="slide-photo"><div role="img" aria-label="Fanned collage of photo booth print strips from a party"></div></div>
  <h1 class="slide-title">PLANNING AN EVENT?</h1>
  <p class="slide-copy">The Trevo SnapKiosk experience captures the essence of your party with ‘instant prints’ that create a buzz at your event while providing a memorable keepsake for your guests. The digital images allow you to share and create masterpieces with hish-res digital prints. Our trained photo booth hosts are on-site the entire time to make sure you have a worry free event.</p>
  <a class="know-more">KNOW MORE
    <svg width="20" height="20" viewBox="0 0 20 20"><circle cx="10" cy="10" r="8.5" fill="none" stroke="#fff" stroke-width="2"/><path d="M6 10h7M10 6.5l3.5 3.5-3.5 3.5" fill="none" stroke="#fff" stroke-width="2"/></svg>
  </a>
  <div class="dots"><span class="active"></span><span></span><span></span><span></span><span></span><span></span></div>
</section>

<h2 class="section-title">TESTIMONIAL</h2>
<div class="rule" style="top:574px"></div>

<p class="quote" style="top:586px">Lorem ipsum dolor sit amet, consectetur adipiscing elit. Nullam sed tortor a risus auctor aliquet. Maecenas malesuada vehicula justo. Phasellus gravida ante a erat laoreet porta. Nam vestibulum placerat lacus non molestie. Aliquam nec sem dolor. Nunc nec eleifend sem. Curabitur et elit velit. Nullam dictum venenatis magna in vestibulum. Nulla dui ante, luctus eget faucibus sed, vestibulum sit amet metus. Nulla eu quam mauris. In consectetur massa non sapien facilisis egestas hendrerit velit consequat. Vivamus eu risus ante. Quisque posuere fringilla risus, id imperdiet odio consectetur sit amet. Ut nec est nec nunc vehicula vulputate. Donec dapibus molestie arcu, ut tincidunt urna fermentum nec. Fusce dictum, erat ut vulputate porttitor, velit velit bibendum eros, a auctor odio sem eu justo.</p>
<div class="portrait" style="top:586px"><div role="img" aria-label="Portrait of a client" style="background:linear-gradient(90deg,#2b2420,#b98f72 55%,#6b5443)"></div></div>
<div class="rule" style="top:723px"></div>
<p class="author" style="top:733px">Colm Ardley, CEO Brightleaf Studio</p>

<p class="quote" style="top:778px">Lorem ipsum dolor sit amet, consectetur adipiscing elit. Nullam sed tortor a risus auctor aliquet. Maecenas malesuada vehicula justo. Phasellus gravida ante a erat laoreet porta. Nam vestibulum placerat lacus non molestie. Aliquam nec sem dolor. Nunc nec eleifend sem. Curabitur et elit velit. Nullam dictum venenatis magna in vestibulum. Nulla dui ante, luctus eget faucibus sed, vestibulum sit amet metus. Nulla eu quam mauris. In consectetur massa non sapien facilisis egestas hendrerit velit consequat. Vivamus eu risus ante. Quisque posuere fringilla risus, id imperdiet odio consectetur sit amet. Ut nec est nec nunc vehicula vulputate. Donec dapibus molestie arcu, ut tincidunt urna fermentum nec. Fusce dictum, erat ut vulputate porttitor, velit velit bibendum eros, a auctor odio sem eu justo.</p>
<div class="portrait" style="top:779px"><div role="img" aria-label="Portrait of a client" style="background:linear-gradient(90deg,#8fbf63,#c96b4a 45%,#e9b9a0)"></div></div>
<div class="rule" style="top:913px"></div>
<p class="author" style="top:923px">Maren Holloway, CEO Kestrel Works Ltd</p>

<p class="quote" style="top:966px">Lorem ipsum dolor sit amet, consectetur adipiscing elit. Nullam sed tortor a risus auctor aliquet. Maecenas malesuada vehicula justo. Phasellus gravida ante a erat laoreet porta. Nam vestibulum placerat lacus non molestie. Aliquam nec sem dolor. Nunc nec eleifend sem. Curabitur et elit velit. Nullam dictum venenatis magna in vestibulum. Nulla dui ante, luctus eget faucibus sed, vestibulum sit amet metus. Nulla eu quam mauris. In consectetur massa non sapien facilisis egestas hendrerit velit consequat. Vivamus eu risus ante. Quisque posuere fringilla risus, id imperdiet odio consectetur sit amet. Ut nec est nec nunc vehicula vulputate. Donec dapibus molestie arcu, ut tincidunt urna fermentum nec. Fusce dictum, erat ut vulputate porttitor, velit velit bibendum eros, a auctor odio sem eu justo.</p>
<div class="portrait" style="top:966px"><div role="img" aria-label="Portrait of a client" style="background:linear-gradient(90deg,#7a4a2c,#e0a27a 50%,#d9c2a8)"></div></div>
<div class="rule" style="top:1102px"></div>
<p class="author" style="top:1113px">Dario Venn, CEO Brightleaf Studio</p>

<footer class="site-footer">
  <p class="copyright">©2012, trevosnapkiosk.com, All Rights Reserved &nbsp;|&nbsp; Terms &amp; Conditions</p>
  <p class="keep-touch">KEEP IN TOUCH</p>
  <div class="social"><span></span><span></span><span></span><span></span></div>
</footer>
</body>
</html>
```